Business supporting small business needs: Business card, A4 letterhead, A6 postcard, C5& C6envelope

We require stationery designed for a new Australian company called "Tallow Meadow" that provides operational strategy and support to small businesses.

We already have a logo (attached).

We require:
- business card (double-sided)
- A4 letterhead (double-sided)
- A6 postcard - to be used like a with-compliments slip (double-sided)
- C5 envelope
- C6 envelope

We would like the backs of the business card, letterhead and postcard to strongly feature the blue colour from the logo.

The business card, letterhead and postcard must contain:
- Tallow Meadow
- Staff member name
- Website address
- Email address
- Phone number
- Postal address
(I will provide these details to the winner)

The letterhead must also contain the ABN: 57 382 916 204 and company name "Tallow Meadow Pty Ltd".

Our standard font is century gothic.
Updates

Thank you for the designs so far.

Please note that the only change to the logo I am open to, is using an all white logo on a blue background.

I am not open to any other changes to the logo, such as shading, shadows or other colour changes.

Target Market(s)

Small and micro business owners

Industry/Entity Type

Small Business

```html
<!DOCTYPE html>
<html lang="en">
<head>
<meta charset="utf-8">
<title>Tallow Meadow – A6 Postcard</title>
<link rel="stylesheet" href="https://fonts.googleapis.com/css2?family=Questrial&display=swap">
<style>
  :root {
    --stage: #262626;
    --stage-label: #8a8a8a;
    --brand-blue: #27aecf;
    --paper: #ffffff;
    --ink-grey: #7a7a7a;
    --rule-grey: #9a9a9a;
    --font-body: "Questrial", "Century Gothic", sans-serif;
  }
  * { box-sizing: border-box; margin: 0; padding: 0; }
  html, body { width: 1200px; height: 900px; overflow: hidden; }
  body {
    position: relative;
    background: var(--stage);
    font-family: var(--font-body);
  }
  .board-title {
    position: absolute; left: 37px; top: 32px;
    font-size: 21px; font-weight: 400; color: var(--stage-label);
  }
  .side-label {
    position: absolute; font-size: 17px; line-height: 1; color: var(--stage-label);
  }
  .side-label--front { left: 170px; top: 543px; }
  .side-label--back { left: 1022px; top: 802px; }

  .postcard {
    position: absolute;
    overflow: hidden;
  }
  /* Front */
  .postcard--front {
    left: 140px; top: 130px; width: 550px; height: 390px;
    background: var(--brand-blue);
  }
  .postcard__spiral {
    position: absolute; inset: 0;
    background:
      radial-gradient(ellipse 34% 40% at 52% 56%, var(--paper) 0 55%, rgba(255,255,255,0) 100%),
      radial-gradient(ellipse 60% 75% at 55% 55%, rgba(255,255,255,0.55) 0 40%, rgba(255,255,255,0) 75%),
      var(--brand-blue);
  }
  .postcard__name {
    position: absolute; left: 0; right: 0; top: 196px;
    text-align: center;
    font-size: 34px; color: var(--brand-blue);
    letter-spacing: 0.5px;
  }
  /* Back */
  .postcard--back {
    left: 525px; top: 418px; width: 530px; height: 370px;
    background: var(--paper);
  }
  .postcard__wordmark {
    position: absolute; left: 58px; top: 44px;
    font-size: 24px; line-height: 1.05; color: var(--brand-blue);
  }
  .postcard__divider {
    position: absolute; left: 262px; top: 40px;
    width: 1px; height: 300px; background: var(--rule-grey);
  }
  .postcard__address-lines {
    position: absolute; left: 282px; top: 135px; width: 210px;
    list-style: none;
  }
  .postcard__address-lines li {
    height: 35px;
    border-bottom: 1px dotted var(--rule-grey);
  }
  .postcard__contact {
    position: absolute; left: 38px; top: 250px;
    font-size: 10px; line-height: 1.25; color: var(--ink-grey);
    font-style: normal;
  }
</style>
</head>
<body>
  <h1 class="board-title">Postcard</h1>

  <section class="postcard postcard--front" aria-label="Postcard front">
    <div class="postcard__spiral" role="img" aria-label="Large blue and white spiral decoration filling the card"></div>
    <p class="postcard__name">Tallow Meadow</p>
  </section>
  <span class="side-label side-label--front">front</span>

  <section class="postcard postcard--back" aria-label="Postcard back">
    <p class="postcard__wordmark">Tallow<br>Meadow</p>
    <address class="postcard__contact">
      www.tallowmeadow.com<br>
      contact@tallowmeadow.com<br>
      T. 555.018.4720<br>
      418 Orchard Lane<br>
      Ballarat, VIC 3350<br>
      Australia
    </address>
    <div class="postcard__divider"></div>
    <ul class="postcard__address-lines">
      <li></li><li></li><li></li><li></li><li></li><li></li>
    </ul>
  </section>
  <span class="side-label side-label--back">back</span>
</body>
</html>
```